KVRo Business Cards

We need a business card design. We are a Technology (Audio Visual) design, sales and installation company. Looking for a double sided design, clean

Contact Information for Business Card

Clean, modern look, 2 sided

Font styles to use
Sans Serif

```html
<!DOCTYPE html>
<html lang="en">
<head>
<meta charset="utf-8">
<title>KVRo Business Cards</title>
<link href="https://fonts.googleapis.com/css2?family=Open+Sans:wght@400;600;700;800&display=swap" rel="stylesheet">
<style>
  :root {
    --navy: #1b2f3f;
    --ink: #1f2a33;
    --orange: #f28a1a;
    --paper: #ffffff;
    --backdrop: #d9dbde;
    --logo-light: #8a99a6;
  }
  * { margin: 0; padding: 0; box-sizing: border-box; }
  html, body { width: 1200px; height: 800px; overflow: hidden; }
  body {
    background: var(--backdrop);
    font-family: "Open Sans", Arial, sans-serif;
    position: relative;
  }
  .card {
    position: absolute;
    width: 560px;
    height: 320px;
    box-shadow: 0 6px 18px rgba(0,0,0,0.18);
  }
  .card-back {
    left: 480px; top: 50px;
    background: var(--navy);
    display: flex; align-items: center; justify-content: center;
  }
  .card-back .brand {
    font-weight: 800;
    font-size: 76px;
    letter-spacing: -2px;
    color: var(--logo-light);
  }
  .card-front {
    left: 160px; top: 420px;
    background: var(--paper);
  }
  .card-front .brand {
    position: absolute;
    left: 58px; top: 112px;
    font-weight: 800;
    font-size: 58px;
    letter-spacing: -2px;
    color: var(--navy);
    line-height: 1;
  }
  .divider {
    position: absolute;
    left: 258px; top: 80px;
    width: 2px; height: 125px;
    background: var(--orange);
  }
  .contact {
    position: absolute;
    left: 290px; top: 86px;
    color: var(--ink);
  }
  .contact .name {
    font-weight: 700;
    font-size: 20px;
    color: var(--orange);
    line-height: 1.1;
  }
  .contact .role {
    font-size: 15px;
    margin-bottom: 12px;
  }
  .contact-line {
    display: flex; align-items: center; gap: 8px;
    font-size: 16px;
    line-height: 1.4;
  }
  .contact-line svg { width: 15px; height: 15px; flex: none; }
  .address {
    position: absolute;
    left: 58px; bottom: 40px;
    font-size: 16px;
    color: var(--ink);
  }
</style>
</head>
<body>

<section class="card card-back">
  <span class="brand">KVRo</span>
</section>

<section class="card card-front">
  <span class="brand">KVRo</span>
  <div class="divider"></div>
  <div class="contact">
    <p class="name">Daniel Whitford</p>
    <p class="role">President</p>
    <p class="contact-line">
      <svg viewBox="0 0 16 16" aria-hidden="true"><path d="M3.5 1.5l2.5 2.8-1.4 1.8c.9 2 2.5 3.6 4.5 4.5l1.8-1.4 2.8 2.5-1.6 2.1C6.5 13.6 2.4 9.5 1.4 3.1z" fill="var(--orange)"/></svg>
      (555) 214-0387
    </p>
    <p class="contact-line">
      <svg viewBox="0 0 16 16" aria-hidden="true"><rect x="1.5" y="3.5" width="13" height="9" fill="none" stroke="var(--orange)" stroke-width="1.4"/><path d="M1.5 3.5l6.5 5 6.5-5" fill="none" stroke="var(--orange)" stroke-width="1.4"/></svg>
      sales@kvro.tech
    </p>
    <p class="contact-line">
      <svg viewBox="0 0 16 16" aria-hidden="true"><g fill="none" stroke="var(--orange)" stroke-width="1.3"><circle cx="8" cy="8" r="6.5"/><ellipse cx="8" cy="8" rx="3" ry="6.5"/><path d="M1.5 8h13M2.5 4.8h11M2.5 11.2h11"/></g></svg>
      www.kvro.tech
    </p>
  </div>
  <p class="address">1187 Larkfield Ct. Suite 200, Alder Springs, Georgia 30412</p>
</section>

</body>
</html>
```